Velmira sailing boat for love and romance seekers*

We will pay extra 200$ for the winning design! So, we have a sailing boat, Harlow 58 KT called Velmira, which we’d like to give for charter in Turkey and maybe other countries. Need a dedicated web page, with gallery, calendar, videos, customer reviews, possibility to pay down payment, legal disclosures and in 3 languages (English, Russian and Turkish). Also, there should be info on toys and crew. We can also agree on a monthly fee for maintenance and updates. It’s really important to show the details, so that potential customers can see clearly that the boat is in perfect shape. If needed, we can even make a 3D of the interior, or any other materials that you might need. People should also have the possibility to see the sailing routes that they can chose and experience while cruising. Additionally, we can organize diving tours, surfing lessons, and any other activities.

Target Market(s)

Family with kids. Those people that are looking for more luxury than what’s usually offered with other boats. This is a middle segment between usual boats and super luxury boats. Also, it’s for those people that want romance, love and are looking for Unforgetable experiences with their family.

Coding

Coded - Design and coding required

Number of Pages Required

3 page

Font styles to use
Sans Serif

Requirements
Must have
• Boat has lots of options, and we have a tender boat with which one can waterski, pull ringos and other toys. It’s big enough to carry all guests at the same time and comfortable to reach safely any remote beach location. We have brand new snorkeling and diving equipment, new paddle and surfing boards, new dartino, Gorvetto and life jackets for all age groups. Also, we should have a page on crew, who they are and whom additionally they can chose (for example cook or cleaning staff).
Nice to have
• We’d like to see a page with will make you dream, feel romantic and in love. To ensure the visitors that our boat is perfect for a dream holiday. Imagine being in a secluded white sand beach bay all alone with your loved ones, in a beautiful luxurious boat. Now stop dreaming and join us to make your dreams come true. Lastly, because of virus, we should also mention that we do proper cleaning of boat after every use (COVID free).

Vēlmirā is a Sanskrit word that means "wandering" or "world", with the connotation of cyclic, circuitous change. It is also the concept of rebirth and "cyclicality of all life, matter, existence", a fundamental belief of most Indian religions. In short, it is the cycle of death and rebirth.
Should not have
• It should not be only for one system, all devices should be able to see that page properly.

```html
<!DOCTYPE html>
<html lang="en">
<head>
<meta charset="utf-8">
<title>Velmira Sailing Boat</title>
<link rel="stylesheet" href="https://fonts.googleapis.com/css2?family=Playfair+Display:wght@700&family=Montserrat:ital,wght@0,400;0,500;0,600;1,400&display=swap">
<style>
:root{
  --red:#c8102e;
  --navy:#0b1a3d;
  --ink:#141414;
  --grey:#cfcfcf;
  --text:#333;
  --blue:#0e4f78;
  --foot:#0c0c0e;
  --serif:'Playfair Display', Georgia, serif;
  --sans:'Montserrat', Arial, sans-serif;
}
*{margin:0;padding:0;box-sizing:border-box}
html,body{width:1200px;height:3683px;overflow:hidden;background:#fff}
body{position:relative;font-family:var(--sans);color:var(--text)}
.abs{position:absolute}
.serif{font-family:var(--serif);font-weight:700;color:var(--ink)}
.rule{position:absolute;height:2px;width:105px;background:linear-gradient(90deg,var(--red) 0 45%,var(--grey) 45% 100%)}
.btn{position:absolute;display:flex;align-items:center;justify-content:center;border-radius:20px;color:#fff;font-size:11px;font-weight:500;letter-spacing:.2px;background:var(--red);white-space:nowrap}
.nav{position:absolute;font-size:11px;font-weight:500;color:#111;letter-spacing:.2px;white-space:nowrap}
.center{left:0;width:1200px;text-align:center}

/* header */
.logo{position:absolute;display:flex;align-items:center;gap:10px}
.logo-dot{width:40px;height:40px;border-radius:50%;background:#c9a27a}
.logo-name{font-family:var(--serif);font-weight:700;font-size:26px;color:#1a1a1a}
.contact{position:absolute;top:27px;font-size:11px;color:#222;display:flex;align-items:center;gap:10px;white-space:nowrap}
.lang{position:absolute;left:965px;top:18px;width:78px;height:35px;border-radius:18px;background:#fff;box-shadow:0 2px 8px rgba(0,0,0,.12);display:flex;align-items:center;gap:6px;padding-left:8px;font-size:10px;font-weight:500}
.lang-dot{width:20px;height:20px;border-radius:50%;background:linear-gradient(180deg,#d22 0 50%,#2b3c8c 50%)}

/* hero */
.hero{position:absolute;left:0;top:128px;width:1200px;height:525px;background:radial-gradient(ellipse at 30% 45%,#3d4f78 0%,#1c2b52 45%,#0e1836 100%)}
.hero-wake{position:absolute;left:0;top:0;width:700px;height:525px;background:linear-gradient(135deg,rgba(255,255,255,.28),rgba(255,255,255,.05) 60%,transparent)}
.hero-ghost{position:absolute;font-family:var(--serif);font-weight:700;font-size:110px;color:rgba(255,255,255,.05);line-height:1}
.hero h1{position:absolute;left:600px;width:500px;top:185px;text-align:center;font-family:var(--serif);font-size:52px;color:#fff}
.hero p{position:absolute;left:600px;width:500px;text-align:center;font-size:11px;color:#fff}
.dots{position:absolute;display:flex;gap:9px}
.dots i{width:7px;height:7px;border-radius:50%;background:#fff}
.dots i.on{background:var(--red)}

/* about */
.about-text{position:absolute;left:157px;top:840px;width:400px;font-size:11.5px;line-height:22px;color:#222}
.feature{position:absolute;top:955px;width:70px;text-align:center;font-size:11px;color:#222}
.feature svg{display:block;margin:0 auto 14px}
.photo{position:absolute}

/* featured */
.featured{position:absolute;left:0;top:1123px;width:1200px;height:499px;background:var(--blue)}
.featured-photo{position:absolute;left:700px;top:0;width:500px;height:499px;background:linear-gradient(160deg,#e9e6dc,#c9c6bd 40%,#8d9aa8 70%,#dde1e6)}
.service{position:absolute;top:205px;width:180px;text-align:center;color:#fff;font-size:15px}
.service .ring{width:102px;height:102px;border-radius:50%;background:#fff;margin:0 auto 18px;display:flex;align-items:center;justify-content:center}

/* gallery */
.arrow{position:absolute;top:1953px;width:48px;height:58px;border:1px solid #222;background:#fff;display:flex;align-items:center;justify-content:center}

/* video */
.video{position:absolute;left:0;top:2282px;width:1200px;height:435px;background:linear-gradient(180deg,#4b4f6e 0%,#5e6078 40%,#3b4464 75%,#2a3350 100%)}

/* testimonial */
.quote{position:absolute;left:270px;width:660px;top:2975px;text-align:center;font-size:11.5px;font-style:italic;line-height:25px;color:#333}
.avatar{position:absolute;left:552px;top:3078px;width:96px;height:96px;border-radius:50%;background:linear-gradient(160deg,#d9d9d9,#9a9a9a)}

/* footer */
.footer{position:absolute;left:0;top:3316px;width:1200px;height:367px;background:var(--foot)}
.footer .nav{color:#fff}
.social{position:absolute;top:3549px;width:35px;height:35px;border-radius:50%;background:var(--red)}
</style>
</head>
<body>

<!-- Header -->
<header>
  <div class="logo" style="left:160px;top:42px">
    <span class="logo-dot"></span>
    <span class="logo-name">Velmira</span>
  </div>
  <div class="contact" style="left:540px">
    <svg width="18" height="18" viewBox="0 0 24 24" fill="none" stroke="#888" stroke-width="1.4"><path d="M5 3h4l2 5-3 2a12 12 0 0 0 6 6l2-3 5 2v4a2 2 0 0 1-2 2A18 18 0 0 1 3 5a2 2 0 0 1 2-2z"/></svg>
    555-204-718-3
  </div>
  <div class="contact" style="left:678px;top:25px">
    <svg width="20" height="14" viewBox="0 0 20 14" fill="none" stroke="#888" stroke-width="1.2"><rect x=".6" y=".6" width="18.8" height="12.8"/><path d="M.6.6 10 8 19.4.6"/></svg>
    info@velmira.com
  </div>
  <div class="btn" style="left:842px;top:17px;width:114px;height:36px;background:var(--navy)">BOOK NOW</div>
  <div class="lang"><span class="lang-dot"></span>ENG
    <svg width="8" height="6" viewBox="0 0 8 6"><path d="M0 0h8L4 5z" fill="#111"/></svg></div>
  <div class="abs" style="left:430px;top:68px;width:628px;height:1px;background:#ddd"></div>
  <nav>
    <span class="nav" style="left:443px;top:93px">HOME</span>
    <span class="nav" style="left:534px;top:93px">ABOUT US</span>
    <span class="nav" style="left:649px;top:93px">OUR BOATS</span>
    <span class="nav" style="left:771px;top:93px">GALLERY</span>
    <span class="nav" style="left:877px;top:93px">VIDEOS</span>
    <span class="nav" style="left:976px;top:93px">CONTACT US</span>
  </nav>
</header>

<!-- Hero -->
<section class="hero" role="img" aria-label="Motor yacht cruising across deep blue sea with white wake">
  <div class="hero-wake"></div>
  <span class="hero-ghost" style="left:745px;top:70px">find</span>
  <span class="hero-ghost" style="left:715px;top:330px">yacht</span>
  <h1>Luxurt Yacht</h1>
  <p style="top:253px">Quisque bibendum tellus vitae elit tincidunt, et dignissim massa imperdiet.</p>
  <p style="top:277px">Nam ullamcorper, sem eget consectetur varius</p>
  <div class="btn" style="left:792px;top:314px;width:114px;height:35px">READ MORE</div>
  <div class="dots" style="left:580px;top:473px"><i></i><i class="on"></i><i></i></div>
</section>

<!-- About -->
<section>
  <h2 class="serif abs" style="left:157px;top:750px;font-size:44px">About Us</h2>
  <div class="rule" style="left:157px;top:815px;width:105px"></div>
  <p class="about-text">Sed in mollis sapien, vitae aliquet lorem. Nulla facilisi. Nullam sollicitudin enim nunc, eu scelerisque arcu semper eget. Integer condimentum arcu sit amet libero pretium, quis accumsan turpis pulvinar. Pellentesque ornare eu turpis tincidunt elementum.</p>
  <div class="feature" style="left:142px">
    <svg width="36" height="36" viewBox="0 0 36 36" fill="none" stroke="var(--red)" stroke-width="1.4"><path d="M6 4v16a6 6 0 0 0 12 0"/><path d="M12 4l20 26"/><path d="M22 24l6 2"/></svg>Fishing</div>
  <div class="feature" style="left:241px">
    <svg width="36" height="36" viewBox="0 0 36 36" fill="none" stroke="var(--red)" stroke-width="1.4"><path d="M6 8h22l-11 12z"/><path d="M17 20v11M11 31h12"/><circle cx="27" cy="6" r="3"/></svg>Celebrate</div>
  <div class="feature" style="left:336px">
    <svg width="36" height="36" viewBox="0 0 36 36" fill="none" stroke="var(--red)" stroke-width="1.4"><path d="M18 3v24M18 5l10 18H18M16 9 8 23h8"/><path d="M4 27h28l-4 5H8z"/></svg>Sailing</div>
  <div class="feature" style="left:434px">
    <svg width="36" height="36" viewBox="0 0 36 36" fill="none" stroke="var(--red)" stroke-width="1.4"><path d="M8 30C4 18 10 6 16 4c2 10-2 20-8 26zM28 30c4-12-2-24-8-26-2 10 2 20 8 26z"/></svg>Waterspot</div>
  <div class="photo" role="img" aria-label="Sailing yacht anchored in a turquoise bay below green hills" style="left:588px;top:724px;width:470px;height:331px;background:linear-gradient(180deg,#8fb8e6 0%,#5a7a4c 10%,#4a6338 45%,#8a9680 60%,#1aa3c9 72%,#0d7fb2 100%)"></div>
</section>

<!-- Featured Boat -->
<section class="featured">
  <div class="featured-photo" role="img" aria-label="Couple relaxing together on a white yacht deck seen from above"></div>
  <h2 class="serif abs" style="left:0;width:815px;text-align:center;top:72px;font-size:42px;color:#fff">Featured Boat</h2>
  <div class="rule" style="left:355px;top:138px"></div>
  <div class="service" style="left:135px">
    <div class="ring"><svg width="46" height="46" viewBox="0 0 46 46" fill="none" stroke="#222" stroke-width="1.5"><circle cx="23" cy="23" r="13"/><circle cx="23" cy="23" r="5"/><path d="M23 2v42M2 23h42M8 8l30 30M38 8 8 38"/></svg></div>Yacht Charters</div>
  <div class="service" style="left:317px">
    <div class="ring"><svg width="46" height="46" viewBox="0 0 46 46" fill="none" stroke="#222" stroke-width="1.5"><path d="M6 28h34l-5 10H11z"/><path d="M11 28V20h24v8M16 20v-6h14v6M21 14V8h4v6"/><path d="M4 42q5-3 10 0t10 0 10 0 10 0"/></svg></div>Yacht Sales</div>
  <div class="service" style="left:504px">
    <div class="ring"><svg width="46" height="46" viewBox="0 0 46 46" fill="none" stroke="#222" stroke-width="1.5"><circle cx="23" cy="8" r="4"/><path d="M23 12v28M15 18h16M8 28a15 12 0 0 0 30 0M8 28l-3 4M38 28l3 4"/></svg></div>Yacht Management</div>
  <div class="btn" style="left:347px;top:389px;width:114px;height:36px">READ MORE</div>
</section>

<!-- Gallery -->
<section>
  <h2 class="serif abs center" style="top:1695px;font-size:44px">Our Gallery</h2>
  <div class="rule" style="left:547px;top:1765px"></div>
  <div class="photo" role="img" aria-label="Yacht helm and cockpit interior" style="left:149px;top:1886px;width:205px;height:228px;background:linear-gradient(135deg,#e8e2d8,#f4f1ec 60%,#e3ddd3);opacity:.9"></div>
  <div class="photo" role="img" aria-label="Coastline with a small boat on clear blue water" style="left:848px;top:1886px;width:196px;height:228px;background:linear-gradient(180deg,#f3f6f8 0%,#c9d5cf 35%,#a9dbe6 70%,#d7e6ea 100%);opacity:.9"></div>
  <div class="photo" role="img" aria-label="Sailing yacht anchored in a turquoise bay below green hills" style="left:353px;top:1829px;width:495px;height:344px;background:linear-gradient(180deg,#8fb8e6 0%,#5a7a4c 10%,#4a6338 45%,#8a9680 60%,#1aa3c9 72%,#0d7fb2 100%)"></div>
  <div class="arrow" style="left:0"><svg width="14" height="22" viewBox="0 0 14 22" fill="none" stroke="#111" stroke-width="2.5"><path d="M12 2 3 11l9 9"/></svg></div>
  <div class="arrow" style="left:1147px;width:53px"><svg width="14" height="22" viewBox="0 0 14 22" fill="none" stroke="#111" stroke-width="2.5"><path d="M2 2l9 9-9 9"/></svg></div>
</section>

<!-- Video -->
<section class="video" role="img" aria-label="Sailor standing at the bow of a sailing yacht at dusk">
  <p class="abs center" style="top:115px;font-size:22px;color:#fff;font-weight:400">Take a Video Tour</p>
  <h2 class="abs center" style="top:160px;font-family:var(--serif);font-weight:700;font-size:42px;color:#fff">Fun and Adventure Awaits</h2>
  <svg class="abs" style="left:561px;top:250px" width="78" height="78" viewBox="0 0 78 78" fill="none" stroke="#fff" stroke-width="4"><circle cx="39" cy="39" r="35"/><path d="M31 24v30l24-15z" stroke-linejoin="round"/></svg>
</section>

<!-- Testimonials -->
<section>
  <h2 class="serif abs center" style="top:2795px;font-size:44px">What Our Client Says</h2>
  <div class="rule" style="left:547px;top:2865px"></div>
  <svg class="abs" style="left:582px;top:2920px" width="36" height="26" viewBox="0 0 36 26" fill="var(--red)"><circle cx="8" cy="8" r="7"/><path d="M14 9q0 12-12 16 7-6 5-13z"/><circle cx="26" cy="8" r="7"/><path d="M32 9q0 12-12 16 7-6 5-13z"/></svg>
  <p class="quote">Pellentesque aliquam purus ac semper eleifend. Morbi ut hendrerit ligula, ut porttitor nulla. Nullam finibus purus eget convallis eleifend. Vivamus tempus cursus mi quis ornare. Phasellus rhoncus luctus metus, vel faucibus ex varius id. Pellentesque habitant morbi tristique senectus et netus et malesuada fames ac turpis egestas.</p>
  <div class="avatar" role="img" aria-label="Client portrait"></div>
  <h3 class="serif abs center" style="top:3190px;font-size:24px">Marco Delane</h3>
  <p class="abs center" style="top:3229px;font-size:11px;color:#333">Washington DC</p>
  <div class="dots" style="left:580px;top:3266px"><i style="background:#e3e3e3"></i><i class="on"></i><i style="background:#e3e3e3"></i></div>
</section>

<!-- Footer -->
<footer class="footer">
  <div class="logo" style="left:515px;top:100px">
    <span class="logo-dot"></span>
    <span class="logo-name" style="color:#fff">Velmira</span>
  </div>
  <nav>
    <span class="nav" style="left:297px;top:189px">HOME</span>
    <span class="nav" style="left:388px;top:189px">ABOUT US</span>
    <span class="nav" style="left:503px;top:189px">OUR BOATS</span>
    <span class="nav" style="left:625px;top:189px">GALLERY</span>
    <span class="nav" style="left:731px;top:189px">VIDEOS</span>
    <span class="nav" style="left:830px;top:189px">CONTACT US</span>
  </nav>
  <div class="abs" style="left:0;top:309px;width:1200px;height:1px;background:#2c2c30"></div>
  <p class="abs center" style="top:332px;font-size:11px;color:#fff">© Copyright 2020 Velmira Sailing Boat.All Right Reserved</p>
</footer>
<span class="social" style="left:533px"></span>
<span class="social" style="left:584px"></span>
<span class="social" style="left:632px"></span>

</body>
</html>
```